Brochure for medical doctor

I need a brochure for a medical doctor to promote his practice. The brochure should contain his picture, business information (use letterhead from attachment), and the following text:

- Now accepting PI cases on lien!
- Same and next business day appointments available for initial visits, pre-operative clearances, and all other medical needs

- Expedited medical reports sent quickly to your office

Industry/Entity Type

Medical

```html
<!DOCTYPE html>
<html lang="en">
<head>
<meta charset="utf-8">
<title>Maple Grove Medical Center – Flyer</title>
<link href="https://fonts.googleapis.com/css2?family=Oswald:wght@300;500;600&family=Open+Sans:wght@400;600;700&display=swap" rel="stylesheet">
<style>
  :root {
    --red: #d3202a;
    --ink: #1a1a1a;
    --charcoal: #3b3b3d;
    --grey-text: #6e6e6e;
    --page: #ffffff;
    --backdrop: #4a4745;
  }
  * { box-sizing: border-box; margin: 0; padding: 0; }
  html, body { width: 1200px; height: 772px; overflow: hidden; background: var(--backdrop); }
  .flyer {
    position: absolute; left: 314px; top: 16px; width: 572px; height: 740px;
    background: var(--page); overflow: hidden;
    font-family: "Open Sans", sans-serif; color: var(--ink);
  }
  .hero { position: absolute; left: 0; top: 0; width: 572px; height: 430px; }
  .brand {
    position: absolute; left: 0; width: 572px; top: 34px;
    display: flex; justify-content: center; align-items: center; gap: 10px;
  }
  .brand-mark { width: 30px; height: 30px; background: var(--red); }
  .brand-name {
    font-family: "Oswald", sans-serif; font-weight: 600; font-size: 30px;
    letter-spacing: 0.5px; color: var(--charcoal); text-transform: uppercase; line-height: 1;
  }
  .headline {
    position: absolute; left: 0; width: 572px; top: 436px; text-align: center;
    font-family: "Oswald", sans-serif; font-weight: 500; font-size: 38px;
    line-height: 1.2; letter-spacing: -0.5px; text-transform: uppercase;
  }
  .headline .accent { color: var(--red); }
  .intro {
    position: absolute; left: 0; width: 572px; top: 487px; text-align: center;
    font-size: 16.5px; line-height: 22px;
  }
  .reports-pill {
    position: absolute; left: 41px; top: 547px; width: 483px; height: 34px;
    border-radius: 17px; background: var(--red); color: #fff;
    font-weight: 700; font-size: 13.5px; letter-spacing: 0.2px;
    display: flex; align-items: center; justify-content: center;
    box-shadow: 0 3px 6px rgba(0,0,0,0.18);
  }
  .address {
    position: absolute; left: 0; width: 572px; top: 588px; text-align: center; font-size: 13px;
  }
  .hours {
    position: absolute; left: 0; width: 572px; top: 614px; text-align: center;
    font-size: 10px; color: var(--grey-text);
  }
  .contact-band { position: absolute; left: 0; top: 648px; width: 572px; height: 58px; background: var(--charcoal); }
  .call-tab {
    position: absolute; left: 351px; top: 678px; width: 221px; height: 28px;
    background: var(--red); clip-path: polygon(14px 0, 100% 0, 100% 100%, 0 100%);
  }
  .portrait {
    position: absolute; left: 15px; top: 608px; width: 127px; height: 127px; border-radius: 50%;
    border: 4px solid #fff; box-shadow: 0 0 0 1px #cfcfcf;
    background: radial-gradient(circle at 50% 45%, #c9b9a6 0%, #9c8a78 55%, #6f6660 100%);
  }
  .doctor-name {
    position: absolute; left: 155px; top: 656px; color: #fff;
    font-family: "Oswald", sans-serif; font-weight: 300; font-size: 19px; line-height: 1.2;
  }
  .doctor-role { position: absolute; left: 155px; top: 682px; color: #fff; font-size: 10.5px; font-weight: 600; }
  .appointment {
    position: absolute; right: 12px; top: 662px; color: #fff; font-size: 11px; text-transform: uppercase;
  }
  .call-us {
    position: absolute; right: 12px; top: 682px; color: #fff; font-weight: 700; font-size: 14px; letter-spacing: 0.3px;
  }
  .website {
    position: absolute; left: 0; width: 572px; top: 716px; text-align: center;
    font-size: 12px; font-weight: 600; letter-spacing: 0.6px;
  }
  .website .accent { color: var(--red); }
</style>
</head>
<body>
  <main class="flyer">
    <svg class="hero" viewBox="0 0 572 430" role="img" aria-label="Photo of a doctor consulting a patient at a desk with a laptop and stethoscope">
      <defs>
        <linearGradient id="heroTone" x1="0" y1="0" x2="1" y2="1">
          <stop offset="0" stop-color="#e4e9ef"/>
          <stop offset="0.55" stop-color="#b9c6d4"/>
          <stop offset="1" stop-color="#8e99a6"/>
        </linearGradient>
        <linearGradient id="topFade" x1="0" y1="0" x2="0" y2="1">
          <stop offset="0" stop-color="#fff" stop-opacity="1"/>
          <stop offset="0.3" stop-color="#fff" stop-opacity="0.6"/>
          <stop offset="0.55" stop-color="#fff" stop-opacity="0"/>
        </linearGradient>
      </defs>
      <path d="M0 0 H572 V362 C540 410 470 425 400 421 C300 415 230 346 160 344 C100 344 50 358 0 370 Z" fill="url(#heroTone)"/>
      <path d="M0 0 H572 V362 C540 410 470 425 400 421 C300 415 230 346 160 344 C100 344 50 358 0 370 Z" fill="url(#topFade)"/>
      <path d="M0 342 C60 325 130 305 205 318 C150 328 90 366 0 375 Z" fill="#3b3b3d"/>
    </svg>

    <div class="brand">
      <span class="brand-mark"></span>
      <span class="brand-name">Maple Grove Medical Center</span>
    </div>

    <h1 class="headline">Now accepting <span class="accent">PI cases on lien!</span></h1>
    <p class="intro">Same and next business day appointments available for initial visits,<br>pre-operative clearances, and all other medical needs</p>

    <div class="reports-pill">EXPEDITED MEDICAL REPORTS SENT QUICKLY TO YOUR OFFICE</div>

    <p class="address">4120 Linden Ave. Fairview, CA 90210</p>
    <p class="hours">Mon-Fri : 9:00 am - 5:00 pm Saturday &amp; Sunday Closed</p>

    <div class="contact-band"></div>
    <div class="call-tab"></div>
    <div class="portrait" role="img" aria-label="Portrait photo of the physician"></div>
    <p class="doctor-name">Daniel Reyes, M.D.</p>
    <p class="doctor-role">Family Practice Physician</p>
    <p class="appointment">Appointment</p>
    <p class="call-us">CALL US : (555) 014-2200</p>

    <p class="website">www.<span class="accent">MapleGroveMedical</span>.com</p>
  </main>
</body>
</html>
```